Brochure for real estate company

We need the brochure in the attachement re-designed in a consistent way with our website. The text and the structure of the text should not be altered, but addidtional design-elements and other stuff can be added. We're looking for a simple and catchy design as in our website (www.kranich-wohnbau.ch). We need design propositions in file formats where we can always change the text ourselves if that is neccessary later on.

Industry/Entity Type

Real Estate

Font styles to use
Sans Serif

Colors
ec2027
f04a50

```html
<!DOCTYPE html>
<html lang="de">
<head>
<meta charset="utf-8">
<title>Besichtigungen &amp; Unterstützung</title>
<link href="https://fonts.googleapis.com/css2?family=Open+Sans:wght@400;600;700;800&display=swap" rel="stylesheet">
<style>
  :root{
    --red:#ec2027;
    --red-soft:#f04a50;
    --black:#1a1a1a;
    --text:#3a3a3a;
    --line:#d9d9d9;
    --paper:#ffffff;
    --section:#f6f6f6;
  }
  *{box-sizing:border-box;margin:0;padding:0}
  html,body{width:900px;height:1200px;overflow:hidden;background:var(--paper)}
  body{font-family:"Open Sans",Arial,sans-serif;color:var(--text);position:relative}

  .top-rule{position:absolute;top:155px;left:0;width:900px;height:9px;display:flex}
  .top-rule .red{flex:0 0 450px;background:var(--red)}
  .top-rule .dark{flex:1;background:var(--black)}

  .intro-bubble{position:absolute;left:36px;top:204px;width:834px;height:126px}
  .intro-bubble svg{position:absolute;inset:0}
  .intro-text{position:absolute;left:42px;top:28px;right:40px;
    color:var(--red);font-weight:700;font-size:20.5px;line-height:1.45}

  .hero{position:absolute;top:375px;left:0;width:900px;height:330px;display:flex}
  .hero-photo{width:420px;height:330px;
    background:linear-gradient(180deg,#c9dbe8 0%,#b6c9a0 22%,#5f8a3e 45%,#3f6b2a 70%,#8a8f80 100%)}
  .hero-panel{position:relative;flex:1;background:var(--red-soft)}
  .hero-panel .notch{position:absolute;left:0;top:168px}
  .hero-title{position:absolute;left:60px;top:145px;color:#fff;
    font-weight:700;font-size:22px;line-height:1.4}

  .services{position:absolute;top:705px;left:0;width:900px;height:495px;background:var(--section)}
  .service-list{list-style:none;position:absolute;left:48px;top:90px;width:824px}
  .service{display:flex;align-items:flex-start;margin-bottom:31px}
  .service .arrow{flex:0 0 42px;margin-top:3px}
  .service p{font-size:16.5px;line-height:1.5;color:var(--text)}
  .service strong{font-weight:700;color:var(--black)}
</style>
</head>
<body>
  <div class="top-rule"><span class="red"></span><span class="dark"></span></div>

  <div class="intro-bubble">
    <svg width="834" height="126" viewBox="0 0 834 126">
      <path d="M1 1 H833 V106 H642 L628 124 L614 106 H1 Z" fill="#fff" stroke="#d9d9d9" stroke-width="2"/>
      <rect x="0" y="0" width="7" height="107" fill="#ec2027"/>
    </svg>
    <p class="intro-text">Der richtige Umgang mit Menschen ist das Herzstück jeder Vermittlung.<br>Hier richten wir ein besonderes Augenmerk.</p>
  </div>

  <section class="hero">
    <div class="hero-photo" role="img" aria-label="Foto eines gepflegten Gartens mit Rasen, Sträuchern und Natursteinweg vor einem Haus"></div>
    <div class="hero-panel">
      <svg class="notch" width="20" height="36" viewBox="0 0 20 36"><path d="M0 0 L20 18 L0 36 Z" fill="#fff"/></svg>
      <h1 class="hero-title">Besichtigungen &amp;<br>Unterstützung</h1>
    </div>
  </section>

  <section class="services">
    <ul class="service-list">
      <li class="service">
        <svg class="arrow" width="34" height="18" viewBox="0 0 34 18"><rect x="0" y="6" width="22" height="6" rx="3" fill="#ec2027"/><path d="M20 1 L33 9 L20 17 Z" fill="#ec2027"/></svg>
        <p><strong>Geschwindigkeit:</strong> Bei uns gibt es keine Bürozeiten, Interessentenanfragen beantworten wir spätestens sofort - auch am Wochenende.</p>
      </li>
      <li class="service">
        <svg class="arrow" width="34" height="18" viewBox="0 0 34 18"><rect x="0" y="6" width="22" height="6" rx="3" fill="#ec2027"/><path d="M20 1 L33 9 L20 17 Z" fill="#ec2027"/></svg>
        <p><strong>Individuelle Beratung:</strong> Wir führen stets zeitnah zur Anfrage verkaufsaktive Einzelbesichtigungen durch und nehmen uns Zeit für den einzelnen Käufer.</p>
      </li>
      <li class="service">
        <svg class="arrow" width="34" height="18" viewBox="0 0 34 18"><rect x="0" y="6" width="22" height="6" rx="3" fill="#ec2027"/><path d="M20 1 L33 9 L20 17 Z" fill="#ec2027"/></svg>
        <p><strong>Wir stehen zur Seite:</strong> Wir bieten dem potentiellen Käufer eine kostenlose und umfassende Finanzierungsberatung und beschleunigen so die Bankabklärungen.</p>
      </li>
      <li class="service">
        <svg class="arrow" width="34" height="18" viewBox="0 0 34 18"><rect x="0" y="6" width="22" height="6" rx="3" fill="#ec2027"/><path d="M20 1 L33 9 L20 17 Z" fill="#ec2027"/></svg>
        <p><strong>Wir geben Antworten:</strong> Neben einer kompetenten Besichtigung bieten wir eine unkomplizierte Erstberatung zu Renovations- und Machbarkeitsfragen</p>
      </li>
    </ul>
  </section>
</body>
</html>
```